Short term Rentals Marketing agency needs Web design.

We Need a web design for our new company based in Calgary, AB. We are a International Luxury home sharing company (short term rental properties, Villas, Boutique Hotels, Bed & Breakfast, Realtors, Mortgage Brokers). We would like to see designs that look simple, modern and professional. Colors would be bold (red, black, white). The final design should communicate something welcoming, symbolize innovation, and growth. Our goal is to form partnerships with Real Estate, Property Management, Short term Rental Clients to make their lives easier and increase revenue. Vlto Harbor Co. offers a flexible and secure way to market our clients properties while maintaining client satisfaction and amazing customer service. We like how https://plumtrellisads.ca/ is interactive (when you scroll down, text gets larger). Other similar websites for Short Term Rentals is https://www.thekeyhavenfirm.com/, https://stayvorabnb.com/, https://www.nestquill.com/, https://www.roostfinch.com/about-us/, https://lodgewardens.com. We have attached our Logo.

Target Market(s)

short term rental properties, Villas, Boutique Hotels, Bed & Breakfast, Realtors, Mortgage Brokers, property owners

Industry/Entity Type

Real Estate

Coding

Coded - Design and coding required

Number of Pages Required

5+ page

Font styles to use
Sans Serif

Requirements
Must have
• Home Page, About Us page, How it works, Services, Contact us.

We like how https://plumtrellisads.ca/ is interactive (when you scroll down, text gets larger).

We have attached our Webcopy. We would like Call to Action Buttons where they're located in the copy and page.

Must have our Logo Colors.

Other similar websites for Short Term Rentals is https://www.thekeyhavenfirm.com/, https://stayvorabnb.com/, https://www.nestquill.com/, https://www.roostfinch.com/about-us/, https://lodgewardens.com.
Nice to have
• Catchy, Interactive Home page.

Should not have
• Should not be too cluttered

```html
<!DOCTYPE html>
<html lang="en">
<head>
<meta charset="utf-8">
<title>Vlto Harbor Co.</title>
<link href="https://fonts.googleapis.com/css2?family=Roboto:wght@500;700&family=Lato:wght@400;700&display=swap" rel="stylesheet">
<style>
:root{
  --red:#e31e24;
  --dark:#231f20;
  --text:#3a3a3a;
  --muted:#777;
  --light:#f4f6f9;
  --grey:#f0f0f0;
  --white:#fff;
}
*{box-sizing:border-box;margin:0;padding:0}
html,body{width:1200px;height:4003px;overflow:hidden}
body{position:relative;font-family:'Lato',sans-serif;color:var(--text);background:var(--white)}
.abs{position:absolute}
.heading{font-family:'Roboto',sans-serif;font-weight:700;color:var(--dark)}
.btn{position:absolute;display:flex;align-items:center;justify-content:center;font-family:'Lato',sans-serif;font-size:14px;border-radius:3px}
.btn-red{background:var(--red);color:var(--white)}
.btn-white{background:var(--white);color:var(--text)}

/* top bar */
.topbar{left:0;top:0;width:1200px;height:48px;background:var(--dark);color:var(--white);font-size:12px}
.topbar span{position:absolute;top:17px;display:flex;align-items:center;gap:7px}

/* nav */
.nav{left:0;top:48px;width:1200px;height:64px;background:var(--white)}
.brand{position:absolute;display:flex;align-items:center;gap:8px;font-family:'Roboto',sans-serif;font-weight:700}
.brand i{display:block;width:20px;height:20px;background:var(--red)}
.menu{position:absolute;left:434px;top:24px;display:flex;gap:18px;font-size:13px;color:var(--dark)}
.menu .active{color:var(--red)}

/* hero */
.hero{left:0;top:112px;width:1200px;height:696px;background:linear-gradient(120deg,#6b7ea8 0%,#4f6494 45%,#7e8fb8 100%);
  clip-path:path("M0 0 H1200 V660 L180 696 Q60 700 0 632 Z")}
.hero h1{position:absolute;left:106px;top:212px;font-size:53px;line-height:63px;color:var(--white)}
.hero p{position:absolute;left:106px;top:368px;width:600px;font-size:13.5px;line-height:25px;color:var(--white)}
.arrow{position:absolute;top:343px;width:35px;height:35px;border:1.5px solid var(--white);border-radius:3px;display:flex;align-items:center;justify-content:center}

.label{position:absolute;left:0;width:1200px;text-align:center;font-size:12px;color:var(--red)}
.sec-title{position:absolute;left:0;width:1200px;text-align:center;font-size:34px}
.sec-text{position:absolute;left:300px;width:600px;text-align:center;font-size:13px;line-height:24px;color:var(--muted)}

/* steps */
.step{position:absolute;top:1080px;width:300px;text-align:center}
.step .ic{width:62px;height:62px;margin:0 auto;border:1.5px solid var(--red);border-radius:50%;display:flex;align-items:center;justify-content:center}
.step h3{margin-top:20px;font-size:17px}
.step p{margin-top:12px;font-size:13px;line-height:24px;color:var(--muted)}

/* about */
.band-light{left:0;top:1368px;width:1200px;height:649px;background:var(--light)}
.dark-box{background:var(--dark);color:var(--white)}
.dark-box .lbl{position:absolute;left:45px;font-size:11px;color:var(--red)}
.dark-box h2{position:absolute;left:45px;font-size:34px;color:var(--white)}
.dark-box p{position:absolute;left:45px;width:460px;font-size:13px;line-height:24px}
.photo{position:absolute}

/* services */
.card{position:absolute;top:2256px;width:308px;height:420px;background:var(--white);box-shadow:0 2px 14px rgba(0,0,0,.07);text-align:center}
.card.featured{top:2253px;background:var(--dark);color:var(--white)}
.card .img{position:absolute;left:14px;top:14px;width:280px;height:198px}
.card .badge{position:absolute;left:139px;top:184px;width:30px;height:30px;border-radius:50%;background:var(--white);box-shadow:0 1px 5px rgba(0,0,0,.15);display:flex;align-items:center;justify-content:center}
.card h3{position:absolute;left:0;top:228px;width:100%;font-size:17px}
.card.featured h3{color:var(--white)}
.card p{position:absolute;left:30px;top:258px;width:248px;font-size:13px;line-height:24px;color:var(--muted)}
.card.featured p{color:var(--white)}
.card .more{position:absolute;left:27px;top:355px;width:254px;height:40px;border-radius:20px;display:flex;align-items:center;justify-content:center;font-size:14px;font-weight:700}
.card .outline{border:1.5px solid var(--dark);color:var(--dark)}
.card .solid{background:var(--red);color:var(--white)}

.stat{position:absolute;width:200px;height:73px;background:var(--white);color:var(--red);font-family:'Roboto',sans-serif;font-weight:500;font-size:22px;display:flex;align-items:center;justify-content:center}

/* footer */
.footer{left:0;top:3577px;width:1200px;height:367px;background:var(--dark);color:var(--white)}
.footer h4{position:absolute;top:65px;font-family:'Roboto',sans-serif;font-size:19px;font-weight:700}
.footer h4::after{content:"";position:absolute;left:0;top:32px;width:78px;height:2px;background:var(--white)}
.footer ul{position:absolute;top:115px;list-style:none;font-size:13px}
.footer li{height:31px;display:flex;gap:10px}
.footer li::before{content:"›";color:var(--red)}
.social{position:absolute;top:277px;display:flex;gap:8px;left:112px}
.social span{width:26px;height:26px;border-radius:50%;background:var(--red)}
.copy{left:0;top:3944px;width:1200px;height:59px;background:var(--red);color:var(--white);font-size:12px;display:flex;align-items:center;justify-content:center}
</style>
</head>
<body>

<div class="abs topbar">
  <span style="left:112px">
    <svg width="12" height="12" viewBox="0 0 24 24" fill="none" stroke="#fff" stroke-width="2"><path d="M5 3h4l2 5-3 2a12 12 0 0 0 6 6l2-3 5 2v4a2 2 0 0 1-2 2A17 17 0 0 1 3 5a2 2 0 0 1 2-2z"/></svg>
    Call Us: +123 456-789</span>
  <span style="left:274px">
    <svg width="12" height="12" viewBox="0 0 24 24" fill="none" stroke="#fff" stroke-width="2"><rect x="3" y="5" width="18" height="14"/><path d="M3 6l9 7 9-7"/></svg>
    Email: info@example.com</span>
  <span style="right:112px">Opening Timing: 8:00 am - 10:00 pm</span>
</div>

<header class="abs nav">
  <div class="brand" style="left:117px;top:20px;font-size:20px;color:var(--dark)"><i></i>Vlto Harbor Co.</div>
  <nav class="menu">
    <span class="active">Home</span><span>About</span><span>How It Works</span><span>Services ⌄</span><span>Contact</span>
  </nav>
  <div class="btn btn-red" style="left:968px;top:16px;width:120px;height:34px;font-size:13px">Call To Action</div>
</header>

<section class="abs hero" role="img" aria-label="Photo of a hotel bedroom with a made bed and flowers, in cool blue tones">
  <h1 class="heading" style="color:#fff">Partner With Us And Let’s<br>Start Growing Together!</h1>
  <p>Lorem ipsum dolor sit amet consectetur adipisicing elit. Nihil architecto laborum eaque! Deserunt maxime, minus quas molestiae reiciendis esse natus nisi iure.</p>
  <div class="btn btn-red" style="left:106px;top:444px;width:119px;height:41px">Contact Us</div>
  <div class="btn btn-white" style="left:246px;top:444px;width:119px;height:41px">Read More</div>
  <div class="arrow" style="left:26px"><svg width="10" height="10" viewBox="0 0 10 10"><path d="M7 1L3 5l4 4" fill="none" stroke="#fff" stroke-width="2"/></svg></div>
  <div class="arrow" style="left:1139px"><svg width="10" height="10" viewBox="0 0 10 10"><path d="M3 1l4 4-4 4" fill="none" stroke="#fff" stroke-width="2"/></svg></div>
</section>

<div class="label" style="top:874px">How it Works</div>
<h2 class="sec-title heading" style="top:898px">Lorem Ipsum Dolor Sit Amet.</h2>
<p class="sec-text" style="top:954px;left:320px;width:560px">Lorem ipsum dolor sit amet consectetur adipisicing elit. A facilis vel consequatur tempora atque blanditiis exercitationem incidunt, alias corporis quam assumenda dicta, temporibus.</p>

<div class="step" style="left:116px">
  <div class="ic"><svg width="28" height="28" viewBox="0 0 24 24" fill="none" stroke="#e31e24" stroke-width="1.4"><path d="M3 11l9-7 9 7"/><path d="M5 10v10h14V10"/><rect x="10" y="14" width="4" height="6"/></svg></div>
  <h3 class="heading">Lorem Ipsum Dolor Sit.</h3>
  <p>Lorem ipsum dolor sit amet, consectetur adipiscing elit, sed do eiusmod tempor incididunt ut labore dolore</p>
</div>
<div class="step" style="left:450px">
  <div class="ic"><svg width="28" height="28" viewBox="0 0 24 24" fill="none" stroke="#e31e24" stroke-width="1.4"><path d="M12 21s-6-6-6-11a6 6 0 0 1 12 0c0 5-6 11-6 11z"/><circle cx="12" cy="10" r="2.3"/></svg></div>
  <h3 class="heading">Lorem Ipsum Dolor Sit.</h3>
  <p>Lorem ipsum dolor sit amet, consectetur adipiscing elit, sed do eiusmod tempor incididunt ut labore dolore</p>
</div>
<div class="step" style="left:783px">
  <div class="ic"><svg width="28" height="28" viewBox="0 0 24 24" fill="none" stroke="#e31e24" stroke-width="1.4"><path d="M3 18V8M3 14h18v4M21 14v-3a2 2 0 0 0-2-2h-8v5"/><circle cx="7" cy="11" r="1.8"/></svg></div>
  <h3 class="heading">Lorem Ipsum Dolor Sit.</h3>
  <p>Lorem ipsum dolor sit amet, consectetur adipiscing elit, sed do eiusmod tempor incididunt ut labore dolore</p>
</div>

<section class="abs band-light"></section>
<div class="abs dark-box" style="left:112px;top:1497px;width:545px;height:394px">
  <div class="lbl" style="top:49px">About Us</div>
  <h2 class="heading" style="top:70px">Lorem Ipsum Dolor Sit Amet.</h2>
  <p style="top:138px">Lorem ipsum dolor sit amet, consectetur adipiscing elit, sed do eiusmod tempor incididunt dolore magna aliqua. Quis ipsum suspendisse ultrices gravida.</p>
  <p style="top:198px">Lorem ipsum dolor, sit amet consectetur adipisicing elit. Architecto cupiditate eius laboriosam doloremque, accusamus ex adipisci, accusantium incidunt illo ratione, tempore eum ipsum explicabo aliquam iusto sit! Nostrum, at commodi.</p>
  <div class="btn btn-red" style="left:45px;top:304px;width:120px;height:40px">Read More</div>
</div>
<div class="photo" style="left:614px;top:1456px;width:474px;height:474px;background:linear-gradient(160deg,#d9cdbd 0%,#c4b39c 45%,#e8e2d8 100%)" role="img" aria-label="Photo of a bright studio room with a bed, bench seat and laptop on a small table"></div>

<div class="label" style="top:2077px">Service</div>
<h2 class="sec-title heading" style="top:2102px">Lorem Ipsum Dolor Sit Amet.</h2>
<p class="sec-text" style="top:2157px;left:300px">Lorem, ipsum dolor sit amet consectetur adipisicing elit. Maxime vero reprehenderit vel accusantium, facilis architecto consectetur nobis tempore ullam suscipit tenetur mollitia corporis veritatis.</p>

<div class="card" style="left:112px">
  <div class="img" style="background:linear-gradient(180deg,#6f7552 0%,#8b7a55 55%,#a58a5c 100%)" role="img" aria-label="Photo of a bedroom with a ceiling fan and a bed"></div>
  <div class="badge"><svg width="14" height="14" viewBox="0 0 24 24" fill="none" stroke="#e31e24" stroke-width="2"><path d="M3 11l9-7 9 7M5 10v10h14V10"/></svg></div>
  <h3 class="heading">Lorem Ipsum Dolor Sit Amet.</h3>
  <p>Lorem ipsum dolor sit amet, consectetur adipiscing elit, sed do eiusmod tempor incididunt dolor sit amet, consectetur.</p>
  <div class="more outline">Read More</div>
</div>
<div class="card featured" style="left:446px">
  <div class="img" style="background:linear-gradient(170deg,#d8d2c8 0%,#c1b6a6 50%,#ece8e2 100%)" role="img" aria-label="Photo of a hotel room with a wall TV and a bed"></div>
  <div class="badge"><svg width="14" height="14" viewBox="0 0 24 24" fill="none" stroke="#e31e24" stroke-width="2"><path d="M4 19h16M6 19v-5h12v5M8 14V9h8v5"/></svg></div>
  <h3 class="heading">Lorem Ipsum Dolor Sit Amet.</h3>
  <p>Lorem ipsum dolor sit amet, consectetur adipiscing elit, sed do eiusmod tempor incididunt dolor sit amet, consectetur.</p>
  <div class="more solid">Read More</div>
</div>
<div class="card" style="left:780px">
  <div class="img" style="background:linear-gradient(180deg,#6f7552 0%,#8b7a55 55%,#a58a5c 100%)" role="img" aria-label="Photo of a bedroom with a ceiling fan and a bed"></div>
  <div class="badge"><svg width="14" height="14" viewBox="0 0 24 24" fill="none" stroke="#e31e24" stroke-width="2"><path d="M3 18V9M3 14h18v4M21 14v-3H11v3"/></svg></div>
  <h3 class="heading">Lorem Ipsum Dolor Sit Amet.</h3>
  <p>Lorem ipsum dolor sit amet, consectetur adipiscing elit, sed do eiusmod tempor incididunt dolor sit amet, consectetur.</p>
  <div class="more outline">Read More</div>
</div>

<section class="abs" style="left:0;top:2765px;width:1200px;height:551px;background:var(--grey)"></section>
<div class="photo" style="left:614px;top:2765px;width:586px;height:551px;background:linear-gradient(180deg,#66704c 0%,#7f7653 50%,#9c8458 100%)" role="img" aria-label="Photo of a bedroom with a window, ceiling fan and a bed with a fringed cover"></div>
<div class="abs dark-box" style="left:112px;top:2847px;width:545px;height:390px">
  <div class="lbl" style="top:47px">lorem ipsum</div>
  <h2 class="heading" style="top:68px">Lorem Ipsum Dolor Sit Amet.</h2>
  <p style="top:136px">Lorem ipsum dolor sit amet, consectetur adipiscing elit, sed do eiusmod tempor incididunt dolore magna aliqua. Quis ipsum suspendisse ultrices gravida.</p>
  <p style="top:196px">Lorem ipsum dolor, sit amet consectetur adipisicing elit. Architecto cupiditate eius laboriosam doloremque, accusamus ex adipisci, accusantium incidunt illo ratione, tempore eum ipsum explicabo aliquam iusto sit! Nostrum, at commodi.</p>
  <div class="btn btn-red" style="left:45px;top:300px;width:120px;height:40px">Read More</div>
</div>
<div class="stat" style="left:713px;top:2954px">lorem ipsum</div>
<div class="stat" style="left:940px;top:2954px">lorem ipsum</div>
<div class="stat" style="left:713px;top:3055px">lorem ipsum</div>
<div class="stat" style="left:940px;top:3055px">lorem ipsum</div>

<section class="abs" style="left:112px;top:3378px;width:976px;height:137px;background:var(--dark)">
  <div class="abs heading" style="left:45px;top:44px;font-size:18px;color:#fff">Get 50% Off</div>
  <div class="abs heading" style="left:45px;top:72px;font-size:18px;color:var(--red)">Save Money Save Time</div>
  <div class="btn btn-red" style="left:797px;top:42px;width:134px;height:41px">Contact Now</div>
</section>

<footer class="abs footer">
  <div class="brand" style="left:117px;top:64px;font-size:20px;color:#fff"><i></i>Vlto Harbor Co.</div>
  <p class="abs" style="left:112px;top:135px;width:225px;font-size:13px;line-height:24px">Lorem ipsum dolor, sit amet earum consectetur adipisicing elit. Cupiditate rerum quidem fugiat sapiente! Iusto quae perspiciatis, repudiandae ipsam minus et ex, aliquid dolor molestias.</p>
  <div class="social"><span></span><span></span><span></span><span></span></div>

  <h4 style="left:362px">Our Services</h4>
  <ul style="left:366px"><li>Service 1</li><li>Service 2</li><li>Service 3</li><li>Service 4</li><li>Service 5</li><li>Service 6</li></ul>

  <h4 style="left:614px">Quick Links</h4>
  <ul style="left:618px"><li>About</li><li>Services</li><li>How it Works</li><li>Contact</li></ul>

  <h4 style="left:864px">Get In Touch</h4>
  <div class="abs" style="left:864px;top:115px;width:230px;font-size:13px;line-height:24px">
    <div style="display:flex;gap:10px"><svg width="14" height="14" viewBox="0 0 24 24" fill="none" stroke="#e31e24" stroke-width="2" style="margin-top:4px"><path d="M5 3h4l2 5-3 2a12 12 0 0 0 6 6l2-3 5 2v4a2 2 0 0 1-2 2A17 17 0 0 1 3 5a2 2 0 0 1 2-2z"/></svg><div><b>Contact:</b><br>Phone: +123 456-789</div></div>
    <div style="display:flex;gap:10px;margin-top:6px"><svg width="14" height="14" viewBox="0 0 24 24" fill="none" stroke="#e31e24" stroke-width="2" style="margin-top:4px"><rect x="3" y="5" width="18" height="14"/><path d="M3 6l9 7 9-7"/></svg><div><b>Email:</b><br>info@example.com</div></div>
    <div style="display:flex;gap:10px;margin-top:6px"><svg width="14" height="14" viewBox="0 0 24 24" fill="none" stroke="#e31e24" stroke-width="2" style="margin-top:4px"><path d="M12 21s-6-6-6-11a6 6 0 0 1 12 0c0 5-6 11-6 11z"/><circle cx="12" cy="10" r="2"/></svg><div><b>Address:</b><br>Lorem ipsum dolor sit amet, consectetur adipiscing elit. Qui, quo.</div></div>
  </div>
</footer>
<div class="abs copy">© Copyright 2020 Vlto Harbor. All Rights Reserved</div>

</body>
</html>
```